Whitmore Business Card Design

The name of the business is Dara Whitmore, CPA LLC
The service that we offer is Accounting, Tax & Consulting Services. I need it to have the following items:
Dara Whitmore, Principal
Phone Number
Email Address
Physical Address

I have attached the company logo, one in black and one in white. Please provide a design in black background and the other in white background. Please include "Accounting, Tax & Consulting Services". I want the business card to be clean and very professional.

```html
<!DOCTYPE html>
<html lang="en">
<head>
<meta charset="utf-8">
<title>Dara Whitmore, CPA LLC – Business Cards</title>
<link href="https://fonts.googleapis.com/css2?family=Montserrat:wght@400;500;600;700&display=swap" rel="stylesheet">
<style>
  :root{
    --bg:#e8e8ea;
    --card:#ffffff;
    --red:#9a1b20;
    --charcoal:#3a3a3c;
    --grey:#8d8e91;
    --text-grey:#7b7c7f;
  }
  *{margin:0;padding:0;box-sizing:border-box}
  html,body{width:1200px;height:1000px;overflow:hidden}
  body{background:var(--bg);font-family:'Montserrat',sans-serif;position:relative}
  .card{position:absolute;width:722px;height:400px;background:var(--card);overflow:hidden}
  .card--front{left:410px;top:90px}
  .card--back{left:87px;top:537px}
  .card__bands{position:absolute;left:0;width:722px;height:17px}
  .card__bands--bottom{bottom:0}
  .card__bands--top{top:0}
  .brand{position:absolute;left:0;right:0;text-align:center}
  .brand__mark{display:block;margin:0 auto;background:var(--charcoal)}
  .brand__name{color:var(--charcoal);font-weight:600;white-space:nowrap}
  .brand__tagline{color:var(--grey);font-weight:600;letter-spacing:.1em;white-space:nowrap}
  .card--front .brand{top:42px}
  .card--front .brand__mark{width:36px;height:36px;margin-bottom:34px}
  .card--front .brand__name{font-size:19px;line-height:20px}
  .card--front .brand__tagline{font-size:13px;line-height:18px}
  .holder{position:absolute;left:68px;top:228px}
  .holder__name{color:var(--red);font-size:31px;line-height:38px;font-weight:500;letter-spacing:.01em}
  .holder__name strong{font-weight:700}
  .holder__title{color:var(--charcoal);font-size:15px;font-weight:500;letter-spacing:.08em;margin-top:2px}
  .divider{position:absolute;left:396px;top:213px;width:3px;height:93px;background:var(--charcoal)}
  .contact{position:absolute;left:424px;top:214px;list-style:none}
  .contact li{display:flex;align-items:center;height:30px;color:var(--text-grey);font-size:14.5px;letter-spacing:.06em}
  .contact svg{width:12px;height:12px;margin-right:12px;fill:var(--red)}
  .card--back .brand{top:123px}
  .card--back .brand__mark{width:60px;height:60px;margin-bottom:22px}
  .card--back .brand__name{font-size:27px;line-height:30px}
  .card--back .brand__tagline{font-size:20px;line-height:28px}
  .services{position:absolute;left:0;right:0;top:295px;text-align:center;color:#1f1f21;font-size:17px;font-weight:700;letter-spacing:.01em}
</style>
</head>
<body>

<section class="card card--front" aria-label="Business card front">
  <div class="brand">
    <span class="brand__mark"></span>
    <p class="brand__name">DARA WHITMORE, CPA, LLC</p>
    <p class="brand__tagline">CERTIFIED PUBLIC ACCOUNTANT</p>
  </div>
  <div class="holder">
    <p class="holder__name"><strong>DARA</strong> WHITMORE</p>
    <p class="holder__title">PRINCIPAL</p>
  </div>
  <span class="divider"></span>
  <ul class="contact">
    <li><svg viewBox="0 0 24 24"><path d="M6.6 10.8a15 15 0 0 0 6.6 6.6l2.2-2.2c.3-.3.7-.4 1-.2 1.1.4 2.3.6 3.6.6.6 0 1 .4 1 1V20c0 .6-.4 1-1 1A17 17 0 0 1 3 4c0-.6.4-1 1-1h3.5c.6 0 1 .4 1 1 0 1.3.2 2.5.6 3.6.1.3 0 .7-.2 1z"/></svg>+111 2222 1111</li>
    <li><svg viewBox="0 0 24 24"><path d="M2 5h20v14H2zM4 7v.5l8 5 8-5V7l-8 5z"/></svg>info@darawhitmore.com</li>
    <li><svg viewBox="0 0 24 24"><path d="M12 2a6 6 0 0 0-6 6c0 4.5 6 10 6 10s6-5.5 6-10a6 6 0 0 0-6-6zm0 8.2a2.2 2.2 0 1 1 0-4.4 2.2 2.2 0 0 1 0 4.4zM4 20h16v2H4z"/></svg>Your Address Here 00123</li>
  </ul>
  <svg class="card__bands card__bands--bottom" viewBox="0 0 722 17" aria-hidden="true">
    <polygon points="0,0 310,0 360,17 0,17" fill="var(--red)"/>
    <polygon points="360,17 410,0 722,0 722,17" fill="var(--grey)"/>
  </svg>
</section>

<section class="card card--back" aria-label="Business card back">
  <svg class="card__bands card__bands--top" viewBox="0 0 722 17" aria-hidden="true">
    <polygon points="0,0 360,0 313,17 0,17" fill="var(--grey)"/>
    <polygon points="360,0 722,0 722,17 408,17" fill="var(--red)"/>
  </svg>
  <div class="brand">
    <span class="brand__mark"></span>
    <p class="brand__name">DARA WHITMORE, CPA, LLC</p>
    <p class="brand__tagline">CERTIFIED PUBLIC ACCOUNTANT</p>
  </div>
  <p class="services">ACCOUNTING, TAX &amp; CONSULTING SERVICES</p>
  <svg class="card__bands card__bands--bottom" viewBox="0 0 722 17" aria-hidden="true">
    <polygon points="0,0 313,0 360,17 0,17" fill="var(--red)"/>
    <polygon points="360,17 408,0 722,0 722,17" fill="var(--grey)"/>
  </svg>
</section>

</body>
</html>
```